Clever & creative business card needed for a pediatric dentist.

We need a business card for a pediatric dentist that is building a brand-new pediatric dental practice. He is funny, outgoing, and sociable, and he hopes to give his business card to dentists and pediatricians so that he can give them information of where to refer infants, children, and teenagers that need high quality and attainable dental care.

The name of the dental practice is Amber Creek Pediatric Dentistry. Logo design .png / .pdf/ .jpg are provided to aid in the design.

The dentist's last name is Moffat (which sounds like "burger", as in "hamburger” or “cheeseburger"). Since it is pediatric practice, kudos will be given to designs that implement a little joke into the design - but hopefully in a small or hidden way (such as putting something like a cheeseburger on the back of the card, or hiding it an an abstract way).

Thank you!

Please make a design that incorporates colors. It should be fun! Not too serious. It does not have to follow the color scheme of the logos.

```html
<!DOCTYPE html>
<html lang="en">
<head>
<meta charset="utf-8">
<title>Amber Creek Pediatric Dentistry — Business Card</title>
<link href="https://fonts.googleapis.com/css2?family=Open+Sans:wght@400;700&display=swap" rel="stylesheet">
<style>
  :root {
    --bg: #e6e6e2;
    --card-white: #ffffff;
    --card-dark: #3f3f41;
    --green: #2f9e55;
    --green-light: #b7dfb8;
    --green-mid: #6cc07a;
    --green-dark: #20904a;
    --ink: #3a3a3a;
    --text: #5a5a5a;
    --paper-white: #ffffff;
  }
  * { box-sizing: border-box; margin: 0; padding: 0; }
  html, body { width: 1200px; height: 856px; overflow: hidden; }
  body {
    background: var(--bg);
    font-family: "Open Sans", Arial, sans-serif;
    position: relative;
  }
  .card {
    position: absolute;
    left: 280px;
    width: 640px;
    height: 366px;
    box-shadow: 0 6px 18px rgba(0,0,0,0.18);
    overflow: hidden;
  }
  .card--front { top: 42px; background: var(--card-white); }
  .card--back { top: 448px; background: var(--card-dark); }

  .edge-band {
    position: absolute;
    left: 0; right: 0; bottom: 0;
    height: 16px;
    background: linear-gradient(90deg, var(--green-light), var(--green-mid) 50%, var(--green-dark));
  }

  .brand {
    position: absolute;
    display: flex;
    align-items: center;
    gap: 14px;
  }
  .brand__dot {
    width: 34px; height: 34px;
    border-radius: 50%;
    background: var(--green-mid);
    flex: none;
  }
  .brand__name {
    font-weight: 400;
    line-height: 1.2;
  }
  .card--front .brand { left: 44px; top: 122px; width: 250px; }
  .card--front .brand__name { font-size: 22px; color: var(--ink); }

  .card--back .brand { left: 50%; top: 50%; transform: translate(-50%, -50%); width: 330px; }
  .card--back .brand__dot { width: 44px; height: 44px; }
  .card--back .brand__name { font-size: 28px; color: var(--paper-white); }

  .divider {
    position: absolute;
    left: 318px;
    top: 62px;
    width: 2px;
    height: 222px;
    background: var(--green);
  }

  .contact {
    position: absolute;
    left: 346px;
    top: 62px;
    color: var(--text);
    font-size: 17px;
    line-height: 1.5;
  }
  .contact__name {
    color: var(--green);
    font-weight: 700;
    font-size: 25px;
    line-height: 1.2;
    letter-spacing: 0.2px;
  }
  .contact__title { margin-bottom: 8px; }
  .contact__line { display: flex; align-items: center; gap: 8px; }
  .contact__line svg { width: 13px; height: 13px; flex: none; fill: var(--green); }
</style>
</head>
<body>
  <section class="card card--front" aria-label="Business card front">
    <div class="brand">
      <span class="brand__dot"></span>
      <span class="brand__name">Amber Creek Pediatric Dentistry</span>
    </div>
    <div class="divider"></div>
    <div class="contact">
      <div class="contact__name">DANIEL MOFFAT</div>
      <div class="contact__title">President</div>
      <div>1180 Harbor Lane</div>
      <div>Seacliff CA 92601</div>
      <div class="contact__line">
        <svg viewBox="0 0 16 16" aria-hidden="true"><path d="M3.5 1.5l2.5 0 1 3.5-1.6 1.2a8 8 0 0 0 4.4 4.4L11 9l3.5 1v2.5c0 1-1 2-2 2A11 11 0 0 1 1.5 3.5c0-1 1-2 2-2z"/></svg>
        <span>555-014-2280</span>
      </div>
      <div class="contact__line">
        <svg viewBox="0 0 16 16" aria-hidden="true"><path d="M1 3h14v10H1z M1.5 3.5L8 9l6.5-5.5" fill="none" stroke="#2f9e55" stroke-width="1.6"/></svg>
        <span>danielmof@ambercreek.com</span>
      </div>
      <div class="contact__line">
        <svg viewBox="0 0 16 16" aria-hidden="true"><circle cx="8" cy="8" r="6.5" fill="none" stroke="#2f9e55" stroke-width="1.5"/><path d="M1.5 8h13M8 1.5c-3 3.5-3 9.5 0 13M8 1.5c3 3.5 3 9.5 0 13" fill="none" stroke="#2f9e55" stroke-width="1.2"/></svg>
        <span>www.ambercreekdental.com</span>
      </div>
    </div>
    <div class="edge-band"></div>
  </section>

  <section class="card card--back" aria-label="Business card back">
    <div class="brand">
      <span class="brand__dot"></span>
      <span class="brand__name">Amber Creek Pediatric Dentistry</span>
    </div>
  </section>
</body>
</html>
```